One-Page Flat Design for SEO Company [2 DAYS]

We need a one-page flat design for our SEO company. Our current website is http://www.rankloft.com/. We are looking to completely re-design the site using new flat design techniques.
Below are some examples of the type of style we're going after:
http://quormel.com/
http://tobyrand.co.uk/
https://pentaly.co/
http://milesporter.me/
As you can see- flat, clean, minimal. It is very important you follow this type of style.
For colour scheme, you may use one of the pre-made colour palettes from here:
http://www.vornacle.com/blog/inspiration/24-flat-designs-with-compelling-color-palettes
I've attached a wireframe to be followed.
Hi,

```html
<!DOCTYPE html>
<html lang="en">
<head>
<meta charset="utf-8">
<title>RankLoft – SEO services that actually work</title>
<link rel="stylesheet" href="https://fonts.googleapis.com/css2?family=Titillium+Web:wght@400;600;700&family=Open+Sans:wght@400;600;700&family=Roboto:wght@400;700&display=swap">
<style>
:root{
  --coral:#f4655a;
  --coral-bright:#fb6a55;
  --orange:#ff8a4c;
  --teal:#45c4a9;
  --teal-deep:#2fae93;
  --navy:#2e4b63;
  --sky:#7fb5c2;
  --sky-ink:#3a6d7b;
  --white:#ffffff;
  --ink:#222222;
  --muted:#666666;
  --sand:#d9d5cd;
  --sand-ink:#8c8880;
  --hero-a:#3a2430;
  --hero-b:#6d4a52;
  --hero-c:#8a6a6a;
  --head:"Titillium Web",sans-serif;
  --body:"Open Sans",sans-serif;
  --hero-font:"Roboto",sans-serif;
}
*{box-sizing:border-box;margin:0;padding:0}
html,body{width:1200px;height:3750px;overflow:hidden}
body{position:relative;font-family:var(--body);color:var(--ink);background:var(--white)}
section,header,footer{position:absolute;left:0;width:1200px}

/* Hero */
.hero{top:0;height:447px;overflow:hidden}
.hero-photo{position:absolute;inset:0;background:
  radial-gradient(ellipse at 70% 40%,var(--hero-c) 0%,transparent 55%),
  linear-gradient(100deg,var(--hero-a) 0%,var(--hero-b) 55%,#4a3038 100%)}
.nav-bar{position:absolute;top:0;left:0;width:1200px;height:80px;background:rgba(20,12,16,.35);border-bottom:1px solid rgba(255,255,255,.15)}
.brand{position:absolute;left:46px;top:12px;color:var(--white)}
.brand-name{font-family:var(--head);font-weight:700;font-size:34px;line-height:36px;letter-spacing:.5px}
.brand-tag{font-family:var(--body);font-size:11px;letter-spacing:1px;text-transform:uppercase;opacity:.85;margin-top:5px}
.nav{position:absolute;top:30px;right:40px;display:flex;gap:46px;list-style:none}
.nav li{font-family:var(--body);font-size:14px;font-weight:600;letter-spacing:1px;color:var(--white)}
.hero-title{position:absolute;left:40px;top:120px;width:640px;font-family:var(--hero-font);font-weight:700;font-size:56px;line-height:64px;color:var(--white)}
.hero-sub{position:absolute;left:40px;top:268px;width:720px;font-family:var(--hero-font);font-size:21px;line-height:27px;color:rgba(255,255,255,.9)}

/* Shared section type */
.section-title{position:absolute;left:0;width:1200px;text-align:center;font-family:var(--head);font-weight:600;font-size:40px;letter-spacing:2px;text-transform:uppercase}
.section-lead{position:absolute;left:0;width:1200px;text-align:center;font-size:15px;line-height:22px}

/* Features */
.features{top:447px;height:625px;background:var(--coral-bright);color:var(--white)}
.arrow{position:absolute;top:275px}
.feature{position:absolute;width:260px;text-align:center}
.feature-icon{width:170px;height:170px;border-radius:50%;margin:0 auto}
.feature-name{font-family:var(--head);font-weight:700;font-size:21px;letter-spacing:2px;text-transform:uppercase;margin-top:50px}
.feature-text{font-size:13px;line-height:20px;margin-top:14px;padding:0 26px}
.features .feature-icon{background:radial-gradient(circle,rgba(255,255,255,.55) 0%,rgba(255,255,255,.25) 60%)}

/* Plans */
.plans{top:1072px;height:772px;background:var(--teal);color:var(--white)}
.plans .section-title{top:62px}
.plans .section-lead{top:124px}
.plan-frame{position:absolute;left:147px;top:172px;width:915px;height:600px;background:var(--teal-deep);padding:12px 8px 0}
.plan-grid{display:flex;height:100%}
.plan{width:225px;height:100%;text-align:center;padding-top:80px}
.plan--coral{background:var(--coral)}
.plan--orange{background:var(--orange)}
.plan--navy{background:var(--navy)}
.plan--sky{background:var(--sky)}
.plan-name{font-family:var(--head);font-size:24px;font-weight:400;letter-spacing:.5px}
.plan-price{font-size:14px;margin-top:4px}
.plan-features{list-style:none;margin-top:66px;font-size:15px;font-weight:600;line-height:37.5px}
.plan-button{display:inline-block;margin-top:34px;width:137px;height:38px;line-height:34px;border:2px solid var(--white);font-size:14px;letter-spacing:.5px;text-transform:uppercase}
.plan--navy .plan-button{background:var(--white);color:var(--navy)}

/* Call to action */
.cta{top:1844px;height:146px;background:var(--navy);color:var(--white)}
.cta-text{position:absolute;left:181px;top:52px;font-family:var(--head);font-size:28px;color:rgba(255,255,255,.85)}
.cta-button{position:absolute;left:859px;top:52px;width:147px;height:50px;line-height:50px;text-align:center;background:var(--coral-bright);font-weight:700;font-size:14px;letter-spacing:1px}

/* Individual services */
.services{top:1990px;height:641px;background:var(--sky);color:var(--white);border-bottom:4px solid var(--coral-bright)}
.services .section-title{top:52px;color:var(--sky-ink)}
.services .section-lead{top:110px}
.services .feature-icon{background:radial-gradient(circle,#fd8b6f 0%,var(--coral-bright) 60%)}
.services .feature-name{color:var(--sky-ink);margin-top:44px}

/* Contact */
.contact{top:2631px;height:706px;background:var(--white)}
.contact .section-title{top:56px;color:var(--ink)}
.contact-address{position:absolute;left:0;top:116px;width:1200px;text-align:center;font-size:16px;color:var(--muted)}
.field{position:absolute;border:2px solid #9a9a9a;background:var(--white);font-size:15px;color:var(--ink);padding:12px 20px}
.field--name{left:197px;top:191px;width:390px;height:54px}
.field--email{left:616px;top:191px;width:390px;height:54px}
.field--message{left:197px;top:269px;width:809px;height:187px}
.send-button{position:absolute;left:525px;top:512px;width:150px;height:54px;line-height:54px;text-align:center;background:var(--coral-bright);color:var(--white);font-weight:700;font-size:14px;letter-spacing:2px}
.social-links{position:absolute;left:0;top:618px;width:1200px;display:flex;justify-content:center;gap:66px;list-style:none;font-family:var(--head);font-weight:600;font-size:24px}

/* Footer */
.site-footer{top:3337px;height:413px;background:var(--sand);color:var(--sand-ink);text-align:center}
.footer-brand{position:absolute;left:0;top:72px;width:1200px}
.footer-brand .brand-name{font-family:var(--head);font-weight:700;font-size:52px;line-height:56px;color:var(--sand-ink)}
.footer-brand .brand-tag{font-size:16px;letter-spacing:2px;text-transform:uppercase;margin-top:4px;opacity:1}
.footer-text{position:absolute;left:0;top:180px;width:1200px;font-size:15px;line-height:24px}
.footer-dots{position:absolute;left:0;top:288px;width:1200px;display:flex;justify-content:center;gap:32px}
.footer-dots span{width:52px;height:52px;border-radius:50%;background:#a9a59d}
</style>
</head>
<body>

<header class="hero">
  <div class="hero-photo" role="img" aria-label="Blurred photograph of a workspace in deep plum and warm brown tones"></div>
  <div class="nav-bar">
    <div class="brand">
      <div class="brand-name">RankLoft</div>
      <div class="brand-tag">Search growth studio</div>
    </div>
    <ul class="nav">
      <li>HOME</li><li>ABOUT</li><li>WORK</li><li>SERVICES</li><li>TEAM</li><li>CONTACT</li>
    </ul>
  </div>
  <h1 class="hero-title">Finally, SEO services that actually work.</h1>
  <p class="hero-sub">Top-notch SEO services that are guaranteed to boost your search engine rankings. 100% search-engine friendly.</p>
</header>

<section class="features">
  <h2 class="section-title" style="top:60px">Why choose RankLoft</h2>
  <p class="section-lead" style="top:116px">Fusce dapibus, tellus ac cursus commodo, tortor mauris condimentum.<br>Duis mollis, est non commodo luctus, nisi erat porttitor ligula, eget lacinia odio sem nec elit.</p>
  <svg class="arrow" style="left:48px" width="36" height="100" viewBox="0 0 36 100"><polyline points="32,2 4,50 32,98" fill="none" stroke="#fff" stroke-width="2.5"/></svg>
  <svg class="arrow" style="left:1116px" width="36" height="100" viewBox="0 0 36 100"><polyline points="4,2 32,50 4,98" fill="none" stroke="#fff" stroke-width="2.5"/></svg>

  <div class="feature" style="left:217px;top:218px">
    <div class="feature-icon" role="img" aria-label="Illustration of a browser window for branding"></div>
    <div class="feature-name">Branding</div>
    <p class="feature-text">Lorem ipsum dolor sit amet, consectetuer adipiscing elit, sed diam nonummy nibh.</p>
  </div>
  <div class="feature" style="left:476px;top:218px">
    <div class="feature-icon" role="img" aria-label="Illustration of a pencil for design"></div>
    <div class="feature-name">Design</div>
    <p class="feature-text">Sed ut perspiciatis unde omnis iste natus error sit voluptatem.</p>
  </div>
  <div class="feature" style="left:748px;top:218px">
    <div class="feature-icon" role="img" aria-label="Illustration of code brackets for development"></div>
    <div class="feature-name">Development</div>
    <p class="feature-text">At vero eos et accusamus et iusto odio dignissimos qui blanditiis praesentium.</p>
  </div>
</section>

<section class="plans">
  <h2 class="section-title">Select a booster plan</h2>
  <p class="section-lead">Neque porro quisquam est, qui dolorem ipsum quia dolor sit amet</p>
  <div class="plan-frame">
    <div class="plan-grid">
      <div class="plan plan--coral">
        <div class="plan-name">ENTERPRISE</div><div class="plan-price">$40/Month</div>
        <ul class="plan-features"><li>Free feature one</li><li>Unlimited feature two</li><li>Unlimited feature three</li><li>2x feature four</li><li>100x feature five</li></ul>
        <span class="plan-button">Get started</span>
      </div>
      <div class="plan plan--orange">
        <div class="plan-name">ENTERPRISE</div><div class="plan-price">$40/Month</div>
        <ul class="plan-features"><li>Free feature one</li><li>Unlimited feature two</li><li>Unlimited feature three</li><li>2x feature four</li><li>100x feature five</li></ul>
        <span class="plan-button">Get started</span>
      </div>
      <div class="plan plan--navy">
        <div class="plan-name">ENTERPRISE</div><div class="plan-price">$40/Month</div>
        <ul class="plan-features"><li>Free feature one</li><li>Unlimited feature two</li><li>Unlimited feature three</li><li>2x feature four</li><li>100x feature five</li></ul>
        <span class="plan-button">Get started</span>
      </div>
      <div class="plan plan--sky">
        <div class="plan-name">ENTERPRISE</div><div class="plan-price">$40/Month</div>
        <ul class="plan-features"><li>Free feature one</li><li>Unlimited feature two</li><li>Unlimited feature three</li><li>2x feature four</li><li>100x feature five</li></ul>
        <span class="plan-button">Get started</span>
      </div>
    </div>
  </div>
</section>

<section class="cta">
  <p class="cta-text">Duis mollis est non commodo luctus nisi erat porttitor.</p>
  <span class="cta-button">BUTTON</span>
</section>

<section class="services">
  <h2 class="section-title">Individual SEO services</h2>
  <p class="section-lead">Fusce dapibus, tellus ac cursus commodo, tortor mauris condimentum.<br>Duis mollis, est non commodo luctus, nisi erat porttitor ligula, eget lacinia odio sem nec elit.</p>
  <svg class="arrow" style="left:48px;top:262px" width="36" height="100" viewBox="0 0 36 100"><polyline points="32,2 4,50 32,98" fill="none" stroke="#fff" stroke-width="2.5"/></svg>
  <svg class="arrow" style="left:1116px;top:262px" width="36" height="100" viewBox="0 0 36 100"><polyline points="4,2 32,50 4,98" fill="none" stroke="#fff" stroke-width="2.5"/></svg>

  <div class="feature" style="left:217px;top:226px">
    <div class="feature-icon" role="img" aria-label="Illustration of a browser window for branding"></div>
    <div class="feature-name">Branding</div>
    <p class="feature-text">Lorem ipsum dolor sit amet, consectetuer adipiscing elit, sed diam nonummy nibh.</p>
  </div>
  <div class="feature" style="left:476px;top:226px">
    <div class="feature-icon" role="img" aria-label="Illustration of a pencil for design"></div>
    <div class="feature-name">Design</div>
    <p class="feature-text">Sed ut perspiciatis unde omnis iste natus error sit voluptatem.</p>
  </div>
  <div class="feature" style="left:748px;top:226px">
    <div class="feature-icon" role="img" aria-label="Illustration of code brackets for development"></div>
    <div class="feature-name">Development</div>
    <p class="feature-text">At vero eos et accusamus et iusto odio dignissimos qui blanditiis praesentium.</p>
  </div>
</section>

<section class="contact">
  <h2 class="section-title">Get in touch</h2>
  <p class="contact-address">48 Harlow Lane, Suite 210, Brookvale, OR 97301, United States of America. Tel: (503) 555-0187</p>
  <div class="field field--name">Your Name</div>
  <div class="field field--email">Your Email</div>
  <div class="field field--message">Your Message</div>
  <span class="send-button">SEND</span>
  <ul class="social-links"><li>Friendlink</li><li>Chirpline</li><li>Circlely</li><li>Workweave</li></ul>
</section>

<footer class="site-footer">
  <div class="footer-brand">
    <div class="brand-name">RankLoft</div>
    <div class="brand-tag">Search growth studio</div>
  </div>
  <p class="footer-text">Fusce dapibus, tellus ac cursus commodo, tortor mauris condimentum.<br>Duis mollis, est non commodo luctus, nisi erat porttitor ligula.</p>
  <div class="footer-dots"><span></span><span></span><span></span></div>
</footer>

</body>
</html>
```